one page website design - codegrovepartners.net

hello.
need a design for codegrovepartners.net - small community of developers that create web sites, services and products in cooperation with entrepreneurs for free.
The main condition is that the venture should be a startup. Community has the right to reject the project if they dislike it. Their motivation is to help developing new great services and get share in business. It's a kind of angel investment on seed stage made by developers :)

It should be 1 page scrollable (paralax) website
You can find sections and the text at rough mockup attached. You can pick any colors and style, up to you. Images at mockup should be substituted with other ones (you have the right to use) or with icons. But they have to fit the idea of each section well. The position of the text the way it's placed can be also changed.
Basically anything can be implemented not like in mockup :) It was done just to explain the idea.

Please include simple minimalistic logo.
Design has to be responsive and look well from tablets and smartphones.
Please display how errors have to look line at the form in the bottom. Also result of form submission

Result has to in PSD with versions for tablet and smartphone + logo in separate file in PNG with transparent background.

Target Market(s)

startups, community, venture funding, programming, angel investments

Industry/Entity Type

Community

Number of Pages Required

1 page

Requirements
Must have
• Design has to be responsive and look well from tablets and smartphones.
• Result has to in PSD with versions for tablet and smartphone + logo in separate file in PNG with transparent background.
Should not have
• images that used by many other websites on the web

```html
<!DOCTYPE html>
<html lang="en">
<head>
<meta charset="utf-8">
<title>Code Grove Partners</title>
<link href="https://fonts.googleapis.com/css2?family=Questrial&family=Ultra&display=swap" rel="stylesheet">
<style>
:root{
  --green:#8dc63f;
  --green-soft:rgba(141,198,63,.82);
  --blue:#1e88d2;
  --ink:#1d1d1d;
  --muted:#9a9a9a;
  --hero-bg:#f1f1f1;
  --page-bg:#fbfbfb;
  --navy:#34495e;
  --teal:#16a085;
  --purple:#8e44ad;
  --red:#e74c3c;
  --label:#222;
}
*{margin:0;padding:0;box-sizing:border-box}
html,body{width:1200px;height:2542px;overflow:hidden}
body{position:relative;background:var(--page-bg);font-family:"Questrial",Arial,sans-serif;color:var(--ink)}
.abs{position:absolute}
.display{font-family:"Ultra",Georgia,serif;font-weight:400}

/* header & hero */
.hero-band{left:0;top:0;width:1200px;height:597px;background:var(--hero-bg)}
.brand{display:flex;align-items:center;gap:12px}
.brand-mark{width:100px;height:100px;border-radius:50%;background:var(--green)}
.brand-name{font-size:24px;color:var(--ink);white-space:nowrap}
.nav{top:50px;display:flex;font-size:14px}
.nav a{color:var(--ink);text-decoration:none;position:absolute;white-space:nowrap}
.btn{background:var(--blue);color:#fff;border-radius:20px;display:flex;align-items:center;justify-content:center;font-size:14px;box-shadow:0 4px 10px rgba(30,136,210,.3)}
.hero-photo{left:536px;top:119px;width:506px;height:356px;background:linear-gradient(135deg,#7d8f6a,#c9c6b4 45%,#5b6a58)}
.hero-tint{left:459px;top:195px;width:509px;height:356px;background:var(--green-soft)}
.hero-copy{left:232px;top:236px;font-size:23px;line-height:1.4;color:var(--ink)}
.hero-copy .strong{font-family:"Ultra",Georgia,serif;font-size:28px}
.hero-copy .small{font-size:21px}
.hero-line{left:156px;top:501px;width:56px;height:2px;background:var(--green)}
.round{width:30px;height:30px;border-radius:50%;background:var(--blue);display:flex;align-items:center;justify-content:center}

/* how it works */
.section-title{font-size:27px;line-height:1.25}
.step-num{font-family:"Ultra",Georgia,serif;font-size:44px;color:#e6e6e6}
.step-card{width:356px;height:200px}
.step-label{background:var(--label);color:#fff;font-size:18px;padding:4px 10px;white-space:nowrap}
.step-label .accent{font-family:"Ultra",Georgia,serif;color:var(--green)}
.step-note{font-size:13px;line-height:1.4;width:320px}

/* terms */
.terms{left:156px;top:1508px;width:886px;height:319px;background:linear-gradient(120deg,#1d5b8c 0%,#123a5e 45%,#0b2237 100%);color:#fff}
.terms h2{position:absolute;left:78px;top:68px;font-size:27px}
.terms-col{position:absolute;top:132px;font-size:13px}
.terms-col h3{font-size:18px;font-weight:400;margin-bottom:8px}
.terms-col h3 .accent{font-family:"Ultra",Georgia,serif;color:var(--green)}
.terms-col li{list-style:none;display:flex;gap:10px;line-height:18px}
.tick{flex:none;margin-top:3px}

/* contact */
.talk-title{left:0;width:1200px;top:1898px;text-align:center;font-size:27px}
.talk-sub{left:0;width:1200px;top:1940px;text-align:center;font-size:13px;color:var(--muted)}
.green-band{left:0;top:2083px;width:1200px;height:459px;background:var(--green)}
.keys-photo{left:156px;top:1985px;width:886px;height:198px;background:linear-gradient(180deg,#6a6a6a,#3b3b3b)}
.form-card{left:232px;top:2083px;width:736px;height:268px;background:#fff;box-shadow:0 2px 6px rgba(0,0,0,.12)}
.field{position:absolute;border:1px solid #ddd;font-size:12px;color:#9a9a9a;padding:8px 10px;background:#fff}
.upload{position:absolute;right:0;top:0;bottom:0;width:92px;background:#e7e7e7;display:flex;align-items:center;justify-content:center;gap:5px;color:#666}

/* footer */
.foot-brand .brand-mark{background:var(--ink);width:106px;height:106px}
.copy{left:459px;top:2450px;font-size:12px}
.social{width:24px;height:24px;border-radius:50%;border:1.5px solid var(--ink)}
.up{left:1016px;top:2445px;width:27px;height:27px;border-radius:50%;background:var(--ink);display:flex;align-items:center;justify-content:center}
</style>
</head>
<body>

<div class="abs hero-band"></div>

<header>
  <div class="abs brand" style="left:155px;top:17px">
    <div class="brand-mark"></div>
    <span class="brand-name">Code Grove Partners</span>
  </div>
  <nav class="abs nav" style="left:0;top:51px">
    <a style="left:514px">How is Works</a>
    <a style="left:661px">Terms and Projects</a>
    <a style="left:844px">Forum</a>
  </nav>
  <div class="abs btn" style="left:932px;top:44px;width:110px;height:31px">Apply</div>
</header>

<section class="hero">
  <div class="abs hero-photo" role="img" aria-label="Team of developers working together around a table"></div>
  <div class="abs hero-tint"></div>
  <p class="abs hero-copy">
    We are a community of<br>
    <span class="strong">web developers</span> that enjoys<br>
    creating innovative <span class="small">products</span><br>
    <span class="small">and services</span>
  </p>
  <div class="abs hero-line"></div>
  <div class="abs round" style="left:232px;top:487px">
    <svg width="12" height="12" viewBox="0 0 12 12"><path d="M10 6H2M5 3L2 6l3 3" stroke="#fff" stroke-width="1.8" fill="none"/></svg>
  </div>
  <div class="abs round" style="left:277px;top:487px">
    <svg width="12" height="12" viewBox="0 0 12 12"><path d="M2 6h8M7 3l3 3-3 3" stroke="#fff" stroke-width="1.8" fill="none"/></svg>
  </div>
</section>

<section class="how">
  <h2 class="abs section-title display" style="left:231px;top:672px">How<br>It Works</h2>

  <span class="abs step-num" style="left:643px;top:640px">01</span>
  <div class="abs step-card" style="left:612px;top:680px;background:var(--navy)" role="img" aria-label="Light bulb with gears illustrating an idea"></div>
  <div class="abs step-label" style="left:636px;top:861px">You Submit <span class="accent">Idea &amp; Brief.</span></div>
  <p class="abs step-note" style="left:644px;top:895px">with extended marketing plan (if you have already)</p>

  <span class="abs step-num" style="left:264px;top:808px">02</span>
  <div class="abs step-card" style="left:232px;top:848px;background:var(--teal)" role="img" aria-label="Support agent with headset"></div>
  <div class="abs step-label" style="left:252px;top:1028px">Schedule <span class="accent">Callnest Call</span></div>
  <p class="abs step-note" style="left:263px;top:1062px">and discuss it with you</p>

  <span class="abs step-num" style="left:643px;top:975px">03</span>
  <div class="abs step-card" style="left:612px;top:1015px;background:var(--purple)" role="img" aria-label="Team meeting around a table seen from above"></div>
  <div class="abs step-label" style="left:636px;top:1197px">Make <span class="accent">Decision</span></div>
  <p class="abs step-note" style="left:644px;top:1231px">after discuss internally</p>

  <span class="abs step-num" style="left:264px;top:1143px">04</span>
  <div class="abs step-card" style="left:232px;top:1183px;background:var(--red)" role="img" aria-label="Rocket launching from a cloud"></div>
  <div class="abs step-label" style="left:252px;top:1364px">Start the <span class="accent">Project</span></div>
  <p class="abs step-note" style="left:263px;top:1398px">if our decision is positive we proceed with marketing plan</p>
</section>

<section class="abs terms" role="img" aria-label="Hands typing on a laptop under a blue tint">
  <h2 class="display">Terms &amp; Projects</h2>
  <div class="terms-col" style="left:78px">
    <h3><span class="accent">Agreement</span> we sign <span class="accent">Supposes</span> that:</h3>
    <ul>
      <li><svg class="tick" width="12" height="12" viewBox="0 0 12 12"><rect x=".5" y=".5" width="11" height="11" fill="none" stroke="#fff"/><path d="M3 6l2 2 4-5" stroke="#fff" stroke-width="1.6" fill="none"/></svg>We get 40% share in venture</li>
      <li><svg class="tick" width="12" height="12" viewBox="0 0 12 12"><rect x=".5" y=".5" width="11" height="11" fill="none" stroke="#fff"/><path d="M3 6l2 2 4-5" stroke="#fff" stroke-width="1.6" fill="none"/></svg>Project is hosted on our servers</li>
      <li><svg class="tick" width="12" height="12" viewBox="0 0 12 12"><rect x=".5" y=".5" width="11" height="11" fill="none" stroke="#fff"/><path d="M3 6l2 2 4-5" stroke="#fff" stroke-width="1.6" fill="none"/></svg>Domain belongs to our account</li>
      <li><svg class="tick" width="12" height="12" viewBox="0 0 12 12"><rect x=".5" y=".5" width="11" height="11" fill="none" stroke="#fff"/><path d="M3 6l2 2 4-5" stroke="#fff" stroke-width="1.6" fill="none"/></svg>We are responsible for development</li>
      <li><svg class="tick" width="12" height="12" viewBox="0 0 12 12"><rect x=".5" y=".5" width="11" height="11" fill="none" stroke="#fff"/><path d="M3 6l2 2 4-5" stroke="#fff" stroke-width="1.6" fill="none"/></svg>You are responsible for marketing (sales)</li>
    </ul>
  </div>
  <div class="terms-col" style="left:532px">
    <h3>Projects <span class="accent">We Prefer:</span></h3>
    <ul>
      <li><svg class="tick" width="12" height="12" viewBox="0 0 12 12"><rect x=".5" y=".5" width="11" height="11" fill="none" stroke="#fff"/><path d="M3 6l2 2 4-5" stroke="#fff" stroke-width="1.6" fill="none"/></svg>Early proof of concept</li>
      <li><svg class="tick" width="12" height="12" viewBox="0 0 12 12"><rect x=".5" y=".5" width="11" height="11" fill="none" stroke="#fff"/><path d="M3 6l2 2 4-5" stroke="#fff" stroke-width="1.6" fill="none"/></svg>Revenue generation supposed after<br>first version</li>
      <li><svg class="tick" width="12" height="12" viewBox="0 0 12 12"><rect x=".5" y=".5" width="11" height="11" fill="none" stroke="#fff"/><path d="M3 6l2 2 4-5" stroke="#fff" stroke-width="1.6" fill="none"/></svg>B2C service or product</li>
      <li><svg class="tick" width="12" height="12" viewBox="0 0 12 12"><rect x=".5" y=".5" width="11" height="11" fill="none" stroke="#fff"/><path d="M3 6l2 2 4-5" stroke="#fff" stroke-width="1.6" fill="none"/></svg>Advertising based business mode</li>
    </ul>
  </div>
</section>

<section class="contact">
  <h2 class="abs talk-title display">Lets Talk</h2>
  <p class="abs talk-sub">Tell Us about your project ideas or just say hello.</p>
  <div class="abs green-band"></div>
  <div class="abs keys-photo" role="img" aria-label="Close-up of a computer keyboard"></div>
  <form class="abs form-card">
    <div class="field" style="left:75px;top:49px;width:285px;height:31px">Your Name</div>
    <div class="field" style="left:75px;top:97px;width:285px;height:31px">Enter your Email</div>
    <div class="field" style="left:75px;top:143px;width:285px;height:31px">Choose File
      <span class="upload"><svg width="10" height="10" viewBox="0 0 10 10"><path d="M5 7V1M2 4l3-3 3 3M1 9h8" stroke="#666" stroke-width="1.4" fill="none"/></svg>Upload</span>
    </div>
    <div class="field" style="left:375px;top:49px;width:285px;height:124px">Idea Description ...</div>
    <div class="abs btn" style="left:312px;top:187px;width:112px;height:34px">Submit</div>
  </form>
</section>

<footer>
  <div class="abs brand foot-brand" style="left:156px;top:2381px">
    <div class="brand-mark"></div>
    <span class="brand-name">Code Grove Partners</span>
  </div>
  <p class="abs copy">© Code Grove Partners 2016.</p>
  <div class="abs social" style="left:846px;top:2446px" aria-label="Social link"></div>
  <div class="abs social" style="left:877px;top:2446px" aria-label="Social link"></div>
  <div class="abs social" style="left:909px;top:2446px" aria-label="Social link"></div>
  <div class="abs social" style="left:941px;top:2446px" aria-label="Social link"></div>
  <div class="abs up">
    <svg width="12" height="12" viewBox="0 0 12 12"><path d="M6 10V2M3 5l3-3 3 3" stroke="#fff" stroke-width="1.8" fill="none"/></svg>
  </div>
</footer>

</body>
</html>
```